Create a Graphic About YOURSELF and PixelHarbor

PixelHarbor would like you (designers) to create an awesome graphic to promote YOURSELF and your profile on PixelHarbor!

Your graphic should communicate your name, your services and should mention PixelHarbor.

The design should be perfect for sharing on Chatterly. Here's an example of what we'd like http://blog.pixelharbor-example.ca/article/333/pixelharbor-launches-3000-hire-me-social-design-contest

Once you submitted your design, we'd love you to share the design ('advertisement') and promote yourself and PixelHarbor to your friends and potential customers. So make your submissions great and get your friends to vote for your design by 'Liking' it on Chatterly!

Prizes:
$1500 - "PixelHarbor Community" prize awarded to the designer with the most Chatterly 'Likes'
5 x $50 for the next 5 'most liked' designs on Chatterly

$1000 - "Hire Me" prize awarded to the designer who receives the most client invites
5 x $50 for the next 5 'most invited' designers

In summary, this is a great opportunity for you to increase your exposure to PixelHarbor customers and win cash prizes. Show off your design skills and get hired by PixelHarbor customers from around the world!

Target Market(s)

Fans, friends and customers of YOU

Industry/Entity Type

Cash

Requirements
Must have
• 1) Include your PixelHarbor user name on the graphic so customers can find you in the PixelHarbor Designer Directory
2) Include the tagline "Hire Me on PixelHarbor.com!" in your graphic design.
3) Share your design's URL on our Chatterly wall at http://chatterly-example.com/pixelharbor and get your friends to 'like' your design.
Nice to have
• 1) Include a tagline that expresses your design approach/philosophy
2) Artwork dimensions: 403 x 403 px
3) You can submit more than 1 design!
Should not have
• You must own the copyright of any images you use including stock imagery.

```html
<!DOCTYPE html>
<html lang="en">
<head>
<meta charset="utf-8">
<title>Elian Varo – Hire Me on PixelHarbor.com!</title>
<link rel="stylesheet" href="https://fonts.googleapis.com/css2?family=Comfortaa:wght@400;700&family=Questrial&family=Parisienne&display=swap">
<style>
  :root {
    --blue: #1a78be;
    --blue-deep: #0f5c9a;
    --paper: #f3f3f3;
    --pattern-tone: #e6e6e6;
  }
  html, body {
    margin: 0;
    padding: 0;
    width: 1200px;
    height: 1200px;
    overflow: hidden;
    background: #ffffff;
  }
  .poster {
    position: relative;
    width: 1200px;
    height: 1200px;
    overflow: hidden;
  }
  .poster__pattern {
    position: absolute;
    inset: 0;
    background: radial-gradient(circle at 50% 45%, #fafafa 0%, var(--paper) 55%, var(--pattern-tone) 100%);
  }
  .poster__shapes {
    position: absolute;
    inset: 0;
    width: 1200px;
    height: 1200px;
  }
  .brand {
    position: absolute;
    left: 0;
    width: 1200px;
    top: 250px;
    display: flex;
    justify-content: center;
    align-items: center;
    gap: 18px;
  }
  .brand__mark {
    width: 38px;
    height: 38px;
    background: var(--blue);
  }
  .brand__name {
    font-family: "Comfortaa", sans-serif;
    font-weight: 700;
    font-size: 52px;
    color: var(--blue);
    letter-spacing: 2px;
  }
  .services {
    position: absolute;
    left: 0;
    width: 1200px;
    top: 408px;
    margin: 0;
    padding: 0;
    list-style: none;
    text-align: center;
    font-family: "Comfortaa", sans-serif;
    font-weight: 700;
    font-size: 21px;
    letter-spacing: 3px;
    color: var(--blue);
    line-height: 46px;
  }
  .profile {
    position: absolute;
    left: 0;
    width: 1200px;
    top: 770px;
    text-align: center;
    font-family: "Questrial", sans-serif;
    color: var(--blue);
    font-size: 37px;
    line-height: 76px;
  }
  .profile p { margin: 0; }
  .philosophy {
    position: absolute;
    left: 0;
    width: 1200px;
    top: 1070px;
    text-align: center;
    font-family: "Parisienne", cursive;
    font-size: 60px;
    color: var(--blue);
    margin: 0;
  }
</style>
</head>
<body>
<main class="poster">
  <div class="poster__pattern" role="img" aria-label="Soft light grey ornament pattern covering the background"></div>

  <svg class="poster__shapes" viewBox="0 0 403 403" aria-hidden="true">
    <rect class="frame-outer" x="1.5" y="1.5" width="400" height="400" fill="none" stroke="var(--blue)" stroke-width="3"/>
    <rect class="frame-inner" x="5" y="5" width="393" height="393" fill="none" stroke="var(--blue)" stroke-width="0.6" opacity="0.6"/>
    <g class="bracket bracket--top-left" fill="var(--blue)">
      <rect x="105" y="38" width="195" height="5"/>
      <rect x="105" y="38" width="5" height="102"/>
    </g>
    <g class="bracket bracket--bottom-right" fill="var(--blue-deep)">
      <rect x="102" y="233" width="228" height="5"/>
      <rect x="325" y="158" width="5" height="80"/>
    </g>
  </svg>

  <div class="brand">
    <span class="brand__mark"></span>
    <span class="brand__name">elian varo</span>
  </div>

  <ul class="services">
    <li>graphic design</li>
    <li>logo design</li>
    <li>flyer design</li>
    <li>business-card design</li>
    <li>icon design</li>
  </ul>

  <section class="profile">
    <p class="profile__name">elian varo</p>
    <p class="profile__role">freelance graphic designer on pixelharbor.com</p>
    <p class="profile__cta">hire me on PixelHarbor.com!</p>
  </section>

  <p class="philosophy">I see the world as being victorial</p>
</main>
</body>
</html>
```